Home Page Design (+50 More Pages To Winning Designer!)

We have a 50+ page website, but we're starting with the home page. The winning designer will get all 50+ pages to design as a 2nd project, so make sure you do your best!

SoarVane is in the private jet industry and needs a re-designed website.

We have created the structure for the website and content inside of Tavoni.io (THESE ARE ONLY ROUGH A.I. GENERATED WIREFRAMES AND DO NOT NEED TO BE FOLLOWED EXACTLY) - https://www.tavoni.io/app/project/P482915_qRuVwKsLm-DDtaHrYuop72XNc8fkoPzqlrhwDxHkaWm3Tq

Take the content from the 'Home Page' under the 'Wireframe' tab on the Tavoni.io link above, but feel free to re-design the page in a better way as these are only A.I. generated wireframes.

We want a DARK theme.... High quality, luxurious feel, greyscale colors. Attached is a brand guideline (BUT THIS IS NOT A 100% BRAND GUIDELINE, YOU CAN CHANGE COLORS AND FONTS AND MAKE CHANGES IF YOU HAVE BETTER IDEAS) and attached is our logo. We are also attaching some examples of other apps and websites to give you a guideline of what we're looking for for this design project.

The final design MUST communicate luxury using high-quality imagery of large cabin luxurious private jets.

ENTRIES THAT DO NOT FOLLOW THE PROJECT BRIEF WILL BE AUTOMATICALLY DISCARDED. FOLLOW THE INSTRUCTIONS!

Industry/Entity Type

Travel

Number of Pages Required

1 page

Font styles to use
Sans Serif

Colors

Designer to choose colors to be used in the design.

Requirements
Must have
• Follow wireframe and use content in wireframe (see Tavoni.io link)

```html
<!DOCTYPE html>
<html lang="en">
<head>
<meta charset="utf-8">
<title>SoarVane Home Page</title>
<link href="https://fonts.googleapis.com/css2?family=Archivo:wght@400;500;600;700&display=swap" rel="stylesheet">
<style>
:root{
  --board:#262426;
  --page:#141414;
  --panel:#1c1c1c;
  --line:#333;
  --text:#f2f2f2;
  --muted:#8a8a8a;
  --light:#ffffff;
  --ink:#111111;
}
*{margin:0;padding:0;box-sizing:border-box}
html,body{width:1027px;height:1200px;overflow:hidden}
body{background:var(--board);font-family:"Archivo",Arial,sans-serif;color:var(--text);position:relative}
.abs{position:absolute}
.col{position:absolute;background:var(--page);overflow:hidden}
.col-left{left:145px;top:100px;width:346px;height:1100px}
.col-right{left:536px;top:0;width:345px;height:1033px}
.photo{position:absolute}
.tag{position:absolute;font-size:4px;letter-spacing:.9px;color:var(--muted);text-transform:uppercase}
.h2{position:absolute;font-size:11.5px;line-height:12px;font-weight:500;color:var(--text)}
.h2.dark{color:var(--ink)}
.body{position:absolute;font-size:3.6px;line-height:6px;color:var(--muted)}
.btn{position:absolute;height:11px;padding:0 9px;display:flex;align-items:center;font-size:4px;font-weight:600;text-transform:uppercase;letter-spacing:.2px;white-space:nowrap}
.btn-light{background:var(--light);color:var(--ink);clip-path:polygon(4px 0,100% 0,100% 100%,0 100%);border-radius:0 6px 6px 0}
.btn-dark{background:var(--ink);color:var(--light);clip-path:polygon(4px 0,100% 0,100% 100%,0 100%);border-radius:0 6px 6px 0}
.btn-outline{border:.7px solid #9a9a9a;color:var(--light);border-radius:2px 6px 6px 6px}
.btn-outline.on-light{border-color:#555;color:var(--ink)}
.brand{position:absolute;font-size:8px;font-weight:400;color:var(--text);display:flex;align-items:center;gap:2px}
.brand i{display:inline-block;width:4px;height:4px;background:var(--text)}
/* hero */
.hero{position:absolute;left:0;top:0;width:346px;height:194px}
.hero-shade{position:absolute;inset:0;background:radial-gradient(ellipse at 50% 50%,rgba(10,10,10,.75),rgba(10,10,10,.1) 70%)}
.nav a{position:absolute;top:12px;font-size:4px;color:var(--text);text-decoration:none}
.hero-title{position:absolute;left:0;width:346px;top:58px;text-align:center;font-size:15px;line-height:18.5px;font-weight:500}
.hero-text{position:absolute;left:87px;width:172px;top:99px;text-align:center;font-size:3.6px;line-height:6px;color:#c8c8c8}
.checks{position:absolute;left:36px;top:313px;font-size:4px;line-height:8px;color:var(--text);list-style:none}
.checks li{display:flex;align-items:center;gap:3px}
.card-photo{position:absolute;width:86px;height:88px}
.card-cap{position:absolute;width:86px;text-align:center;font-size:5.5px;line-height:7px;font-weight:500}
.card-mid{position:absolute;left:130px;top:448px;width:86px;height:117px;background:linear-gradient(180deg,#2a2a2a,#1e1e1e)}
.acc{position:absolute;left:188px;width:258px;font-size:5.5px;font-weight:500}
.acc-row{position:absolute;left:188px;width:113px;height:.6px;background:var(--line)}
.ring{position:absolute;border-radius:50%;background:rgba(40,40,40,.85);border:.5px solid #2e2e2e;display:flex;flex-direction:column;align-items:center;justify-content:center;text-align:center}
.ring b{font-size:5px;line-height:6.5px;font-weight:500}
.ring span{font-size:3.4px;line-height:4.6px;color:var(--muted);margin-top:3px}
/* cta band: flat light-to-dark field where the jet image sits */
.band{position:absolute;left:0;width:346px;height:156px;overflow:hidden;background:#161616}
.band-image{position:absolute;inset:0;background:
  radial-gradient(ellipse 30% 30% at 50% 62%,rgba(235,235,235,.55),rgba(235,235,235,0) 100%),
  linear-gradient(180deg,#ffffff 0%,#f1f1f1 40%,#bcbcbc 62%,#2a2a2a 85%,#161616 100%)}
.quote{position:absolute;line-height:1;font-weight:700;color:#1f1f1f}
.stars{position:absolute;display:flex;gap:1.5px}
.logo-grid{position:absolute;left:36px;top:369px;width:273px;height:66px;display:grid;grid-template-columns:repeat(5,1fr);grid-template-rows:repeat(3,1fr);border:.5px solid #262626}
.logo-grid div{border:.5px solid #262626;display:flex;align-items:center;justify-content:center;gap:2px;font-size:4.6px;color:#8c8c8c;font-weight:500}
.logo-grid i{display:inline-block;width:4px;height:4px;background:#8c8c8c;border-radius:50%}
.faq{position:absolute;left:74px;width:196px;border:.6px solid #343434;padding:0 7px;font-size:4px;font-weight:500}
.faq .q{display:flex;justify-content:space-between;align-items:center;height:14px}
.faq p{font-size:3.5px;line-height:6px;color:var(--muted);font-weight:400}
.fcol{position:absolute;font-size:3.8px;line-height:8.7px;color:var(--muted)}
.fcol b{display:block;color:var(--text);font-weight:600;line-height:6px;margin-bottom:4px}
.field{position:absolute;height:12px;border:.6px solid #777;display:flex;align-items:center;gap:4px;padding-left:6px;font-size:3.6px;color:var(--muted)}
.social{position:absolute;width:4.5px;height:4.5px;border-radius:50%;background:var(--text)}
</style>
</head>
<body>

<main class="col col-left">

  <section class="hero">
    <div class="photo" role="img" aria-label="Collage of private jet cabins, windows and jets in flight" style="inset:0;background:linear-gradient(160deg,#3a3a3a 0%,#1e1e1e 40%,#2a2a2a 70%,#474747 100%)"></div>
    <div class="hero-shade"></div>
    <div class="brand" style="left:12px;top:10px">SoarVane<i></i></div>
    <nav class="nav">
      <a style="left:83px">Aircraft</a>
      <a style="left:107px">Programs</a>
      <a style="left:136px">Why SoarVane</a>
      <a style="left:173px">Lifestyle ⌄</a>
    </nav>
    <div class="btn btn-outline" style="left:237px;top:9px;padding:0 7px;font-size:3.6px">Featured from blog</div>
    <div class="btn btn-light" style="left:294px;top:9px;padding:0 8px;font-size:3.6px">Article title</div>
    <h1 class="hero-title">Experience The Ultimate<br>in Luxury Jet Travel</h1>
    <p class="hero-text">SoarVane offers fractional jet ownership, jet card programs, private jet lease programs, all access programs, helicopter access programs, and by the seat charter flights. Discover the perfect flight program for your needs.</p>
    <div class="btn btn-light" style="left:132px;top:125px">Explore</div>
    <div class="btn btn-outline" style="left:172px;top:125px">Learn more</div>
  </section>

  <section>
    <div class="tag" style="left:36px;top:224px">Discover</div>
    <h2 class="h2" style="left:35px;top:234px">Experience The<br>Luxury of Fractional<br>Jet Ownership</h2>
    <p class="body" style="left:36px;top:274px;width:124px">With SoarVane's fractional jet ownership program, you can enjoy the benefits of private jet travel without the hassle and expense of owning a whole aircraft. Our program offers flexibility, convenience, and access to a fleet of luxurious jets, allowing you to travel in style and comfort.</p>
    <ul class="checks">
      <li><svg width="5" height="5" viewBox="0 0 10 10"><path d="M1 5l3 3 5-6" stroke="#fff" stroke-width="1.4" fill="none"/></svg>Flexible Ownership Options</li>
      <li><svg width="5" height="5" viewBox="0 0 10 10"><path d="M1 5l3 3 5-6" stroke="#fff" stroke-width="1.4" fill="none"/></svg>Convenient Booking Process</li>
      <li><svg width="5" height="5" viewBox="0 0 10 10"><path d="M1 5l3 3 5-6" stroke="#fff" stroke-width="1.4" fill="none"/></svg>Luxurious Fleet of Jets</li>
    </ul>
    <div class="btn btn-light" style="left:36px;top:347px">Sign up</div>
    <div class="btn btn-outline" style="left:71px;top:347px">Learn more</div>
    <div class="photo" role="img" aria-label="Flight attendant welcoming guests beside a private jet" style="left:183px;top:219px;width:127px;height:140px;background:linear-gradient(150deg,#8a8a8a 0%,#5a5a5a 50%,#2e2e2e 100%)"></div>
    <div class="photo" role="img" aria-label="Private jet front view on a dark runway" style="left:0;top:360px;width:346px;height:70px;background:radial-gradient(ellipse 45% 40% at 52% 60%,#3e3e3e,#1a1a1a 60%,rgba(20,20,20,0) 100%)"></div>
  </section>

  <section>
    <div class="card-photo" role="img" aria-label="Businessman walking beside a private jet" style="left:36px;top:448px;background:linear-gradient(160deg,#9a9a9a,#4a4a4a 60%,#2a2a2a)"></div>
    <div class="card-cap" style="left:36px;top:542px">Flexible Ownership<br>Options Available</div>
    <div class="card-mid">
      <svg class="abs" style="left:29px;top:15px" width="28" height="28" viewBox="0 0 28 28"><circle cx="14" cy="14" r="13.5" fill="none" stroke="#d8d8d8" stroke-width=".8"/><g transform="rotate(-20 14 14)"><rect x="8" y="10" width="12" height="8" rx="1" fill="none" stroke="#d8d8d8" stroke-width=".8"/><line x1="8" y1="12.5" x2="20" y2="12.5" stroke="#d8d8d8" stroke-width=".8"/></g></svg>
      <div class="card-cap" style="left:0;top:55px;width:86px">Convenient Jet<br>Card Programs</div>
      <p class="body" style="left:14px;top:77px;width:58px;text-align:center;font-size:3.4px;line-height:5.6px">Access a fleet of private jets with our exclusive jet card programs, offering flexibility and convenience.</p>
    </div>
    <div class="card-photo" role="img" aria-label="Client signing a lease agreement" style="left:223px;top:448px;background:linear-gradient(160deg,#7a7a7a,#b0b0b0 50%,#5a5a5a)"></div>
    <div class="card-cap" style="left:223px;top:542px">Flexible Lease<br>Programs</div>
  </section>

  <section>
    <div class="photo" role="img" aria-label="Businessman seated in a jet cabin leather chair" style="left:0;top:600px;width:163px;height:155px;background:linear-gradient(120deg,#3c3c3c,#1c1c1c 55%,#2c2c2c)"></div>
    <div class="tag" style="left:188px;top:608px">Experience</div>
    <h2 class="h2" style="left:187px;top:618px">Unparalleled Luxury<br>and Convenience for<br>Private Aviation</h2>
    <p class="body" style="left:188px;top:658px;width:114px">Discover the ultimate in luxury and convenience with SoarVane. Our exclusive private aviation solutions provide you with unparalleled access to the world of private jets, ensuring a seamless and extraordinary travel experience.</p>
    <div class="acc" style="top:692px">Convenience</div>
    <div class="abs" style="left:297px;top:691px;font-size:5px">⌄</div>
    <div class="acc-row" style="top:704px"></div>
    <div class="acc" style="top:710px">Luxury</div>
    <div class="abs" style="left:297px;top:709px;font-size:5px">⌄</div>
    <div class="acc-row" style="top:722px"></div>
    <div class="btn btn-light" style="left:188px;top:735px">Sign up</div>
    <div class="btn btn-outline" style="left:224px;top:735px">Learn more</div>
  </section>

  <section>
    <div class="tag" style="left:37px;top:796px">Luxury</div>
    <h2 class="h2" style="left:37px;top:806px">Experience the<br>Ultimate in Private<br>Jet Travel</h2>
    <p class="body" style="left:37px;top:848px;width:108px">SoarVane offers a wide range of exclusive services to meet your private jet travel needs. From fractional jet ownership to on-demand charter flights, we provide the highest level of luxury and convenience.</p>
    <div class="btn btn-light" style="left:37px;top:882px">Sign up</div>
    <div class="btn btn-outline" style="left:72px;top:882px">Learn more</div>
    <div class="ring" style="left:201px;top:779px;width:78px;height:78px;padding-bottom:24px"><b>On-Demand<br>Charter</b></div>
    <div class="ring" style="left:170px;top:834px;width:70px;height:76px"><b>Global Medical<br>Response &amp;<br>Recovery</b></div>
    <div class="ring" style="left:240px;top:834px;width:70px;height:76px"><b>Fractional Jet<br>Ownership</b><span>Enjoy the benefits of<br>owning a private jet<br>without the hassles.</span></div>
  </section>

  <section class="band" style="top:944px">
    <div class="band-image" role="img" aria-label="Underside view of a large private jet with wings spread"></div>
    <h2 class="h2 dark" style="left:36px;top:22px">Experience Luxury Travel<br>Like Never Before</h2>
    <p class="body" style="left:37px;top:48px;color:#777">Contact us today to book your exclusive jet experience</p>
    <div class="btn btn-dark" style="left:223px;top:36px">Sign up</div>
    <div class="btn btn-outline on-light" style="left:265px;top:36px">Learn more</div>
  </section>
  <div class="quote" style="left:36px;top:1078px;font-size:110px">“</div>
  <div class="stars" style="left:169px;top:1087px">
    <svg width="28" height="5" viewBox="0 0 56 10"><g fill="#fff"><path id="st" d="M5 0l1.5 3.3 3.5.4-2.6 2.4.7 3.5L5 7.8 1.9 9.6l.7-3.5L0 3.7l3.5-.4z"/><use href="#st" x="11.5"/><use href="#st" x="23"/><use href="#st" x="34.5"/><use href="#st" x="46"/></g></svg>
  </div>
</main>

<main class="col col-right">

  <section>
    <p class="body" style="left:37px;top:7px;width:108px">SoarVane offers a wide range of exclusive services to meet your private jet travel needs. From fractional jet ownership to on-demand charter flights, we provide the highest level of luxury and convenience.</p>
    <div class="btn btn-light" style="left:37px;top:41px">Sign up</div>
    <div class="btn btn-outline" style="left:72px;top:41px">Learn more</div>
    <div class="ring" style="left:170px;top:-6px;width:70px;height:76px"><b>Global Medical<br>Response &amp;<br>Recovery</b></div>
    <div class="ring" style="left:240px;top:-6px;width:70px;height:76px"><b>Fractional Jet<br>Ownership</b><span>Enjoy the benefits of<br>owning a private jet<br>without the hassles.</span></div>
  </section>

  <section class="band" style="top:104px;width:345px;height:139px">
    <div class="band-image" role="img" aria-label="Underside view of a large private jet with wings spread"></div>
    <h2 class="h2 dark" style="left:36px;top:18px">Experience Luxury Travel<br>Like Never Before</h2>
    <p class="body" style="left:37px;top:48px;color:#777">Contact us today to book your exclusive jet experience</p>
    <div class="btn btn-dark" style="left:222px;top:31px">Sign up</div>
    <div class="btn btn-outline on-light" style="left:264px;top:31px">Learn more</div>
  </section>

  <section>
    <div class="quote" style="left:32px;top:228px;font-size:170px">“</div>
    <div class="stars" style="left:169px;top:247px">
      <svg width="33" height="6" viewBox="0 0 56 10"><g fill="#fff"><path id="st2" d="M5 0l1.5 3.3 3.5.4-2.6 2.4.7 3.5L5 7.8 1.9 9.6l.7-3.5L0 3.7l3.5-.4z"/><use href="#st2" x="11.5"/><use href="#st2" x="23"/><use href="#st2" x="34.5"/><use href="#st2" x="46"/></g></svg>
    </div>
    <blockquote class="abs" style="left:168px;top:261px;width:140px;font-size:6.6px;line-height:9.8px;font-style:italic">"SoarVane's services have exceeded my expectations. The convenience and luxury of flying with them is unmatched."</blockquote>
    <div class="photo" role="img" aria-label="Portrait of the client" style="left:168px;top:301px;width:18px;height:18px;border-radius:50%;background:#6a6a6a"></div>
    <div class="abs" style="left:192px;top:304px;font-size:5px;font-weight:500">- Marcus Hale</div>
    <div class="abs" style="left:195px;top:311px;font-size:3.5px;color:var(--muted)">CEO, Northfield Group</div>
  </section>

  <section>
    <div class="abs" style="left:0;width:345px;top:353px;text-align:center;font-size:4.2px">Trusted by top-tier companies around the globe</div>
    <div class="logo-grid">
      <div><i></i>Corvale</div><div><i></i>Lumora</div><div><i></i>Vestrin</div><div><i></i>Halden</div><div><i></i>Quorra</div>
      <div><i></i>Ardent</div><div><i></i>Nimbra</div><div><i></i>Solace</div><div><i></i>Tervo</div><div><i></i>Oakline</div>
      <div><i></i>Brisa</div><div><i></i>Kestrel</div><div><i></i>Maren</div><div><i></i>Pylon</div><div><i></i>Auren</div>
    </div>
  </section>

  <section class="abs" style="left:0;top:469px;width:345px;height:93px;background:linear-gradient(90deg,#2a2a2a,#3a3a3a)">
    <div class="photo" role="img" aria-label="Private jet flying above clouds" style="left:170px;top:0;width:175px;height:93px;background:radial-gradient(ellipse at 50% 45%,#bdbdbd,#6a6a6a 55%,#3a3a3a 100%)"></div>
    <h2 class="h2" style="left:36px;top:25px">Subscribe to our Newsletter</h2>
    <p class="body" style="left:37px;top:42px">Stay updated with exclusive offers and industry news.</p>
    <div class="field" style="left:37px;top:55px;width:76px">
      <svg width="6" height="4" viewBox="0 0 12 8"><rect x=".5" y=".5" width="11" height="7" fill="none" stroke="#999" stroke-width=".8"/><path d="M.5 .5l5.5 4 5.5-4" fill="none" stroke="#999" stroke-width=".8"/></svg>Email address
    </div>
    <div class="btn btn-light" style="left:110px;top:55px;height:12px">Join now</div>
  </section>

  <section>
    <h2 class="h2" style="left:0;width:345px;top:584px;text-align:center">Frequently Asked Questions</h2>
    <p class="body" style="left:0;width:345px;top:599px;text-align:center">Find answers to common questions about SoarVane's services and programs.</p>
    <div class="faq" style="top:616px"><div class="q">What is SoarVane?<span>⌄</span></div></div>
    <div class="faq" style="top:633px;height:47px"><div class="q">How it works?<span>⌃</span></div><p>SoarVane works by allowing customers to purchase fractional ownership of a private jet, join jet card programs for a set number of flight hours, lease a private jet for a specific period, or access our all access and helicopter programs. We also offer charter flights where customers can book individual seats on private jets.</p></div>
    <div class="faq" style="top:683px"><div class="q">Why choose SoarVane?<span>⌄</span></div></div>
    <div class="faq" style="top:701px"><div class="q">How to book?<span>⌄</span></div></div>
    <div class="faq" style="top:719px"><div class="q">What are the benefits?<span>⌄</span></div></div>
    <div class="abs" style="left:111px;top:747px;font-size:6px;font-weight:500">Still have questions?</div>
    <div class="abs" style="left:111px;top:756px;font-size:3.6px;color:var(--muted)">Contact us for more information.</div>
    <div class="btn btn-light" style="left:193px;top:749px;padding:0 10px">Contact</div>
  </section>

  <section class="band" style="top:789px;width:345px;height:125px">
    <div class="band-image" role="img" aria-label="Underside view of a large private jet with wings spread"></div>
    <h2 class="h2 dark" style="left:36px;top:16px;line-height:13px">Experience Luxury<br>Travel Like Never<br>Before</h2>
    <p class="body" style="left:192px;top:16px;width:122px;color:#777">Discover the ultimate in private jet travel with SoarVane. Whether you're looking for fractional jet ownership, jet card programs, private jet lease programs, all access programs, helicopter access programs, or by the seat charter flights, we have the perfect solution for your travel needs.</p>
    <div class="btn btn-dark" style="left:192px;top:54px;padding:0 10px">Book</div>
    <div class="btn btn-outline on-light" style="left:227px;top:54px">Contact</div>
  </section>

  <footer>
    <div class="brand" style="left:37px;top:931px">SoarVane<i></i></div>
    <div class="fcol" style="left:97px;top:932px"><b>About Us</b>Charter<br>Fleet<br>Destinations<br>Pricing<br>Contact</div>
    <div class="fcol" style="left:144px;top:932px"><b>Services</b>Private Jets<br>Helicopters<br>Jet Cards<br>Membership<br>FAQ</div>
    <div class="fcol" style="left:192px;top:932px"><b>Terms</b>Privacy<br>Careers<br>Press<br>Blog<br>Support</div>
    <div class="abs" style="left:230px;top:932px;font-size:6.5px;font-weight:500">Subscribe</div>
    <div class="abs" style="left:230px;top:944px;font-size:3.6px;color:var(--muted)">Join our mailing list for the latest updates.</div>
    <div class="field" style="left:231px;top:955px;width:78px;height:11px;border-radius:0 5px 5px 0">
      <svg width="6" height="4" viewBox="0 0 12 8"><rect x=".5" y=".5" width="11" height="7" fill="none" stroke="#999" stroke-width=".8"/><path d="M.5 .5l5.5 4 5.5-4" fill="none" stroke="#999" stroke-width=".8"/></svg>Email address
    </div>
    <div class="btn btn-light" style="left:231px;top:970px">Subscribe</div>
    <div class="abs" style="left:37px;top:1010px;width:272px;height:.6px;background:var(--line)"></div>
    <div class="abs" style="left:37px;top:1020px;font-size:3.6px;color:var(--muted)">©2024 SoarVane. All Rights Reserved. &nbsp;Privacy Policy &nbsp;| &nbsp;Terms of Service &nbsp;| &nbsp;Cookie Settings</div>
    <div class="social" style="left:267px;top:1020px"></div>
    <div class="social" style="left:276px;top:1020px"></div>
    <div class="social" style="left:285px;top:1020px"></div>
    <div class="social" style="left:294px;top:1020px"></div>
    <div class="social" style="left:303px;top:1020px"></div>
  </footer>
</main>

</body>
</html>
```